Luxury Business Card Design for High-End Window Treatments

Gilded Vantages
Custom Plantation Shutters & Architectural Shading Systems

⸻

BACK

Daniel Forsythe
Owner

Custom Interior & Exterior Window Treatments

919-482-7034
gildedvantages.com

I have included a picture that I’m hoping we can use on the back, but I’m also wondering if you can get rid of the ladder? Should we get rid of shutters , shades and blinds underneath Gilded Vantages?

Target Market(s)

High-end residential homeowners, custom home builders, architects, interior designers, and luxury renovation clients seeking premium plantation shutters and motorized architectural shading systems.

Industry/Entity Type

Custom Window treatments

Contact Information for Business Card

Front Gilded Vantages Custom Plantation Shutters Motorized Architectural Shading Systems BACK Daniel Forsythe Owner 919-482-7034 GildedVantages.com Custom Interior & Exterior Window Treatments By Appointment

Requirements
Nice to have
• Not 100% sure on nice to halves or the color but you can definitely check out my website to get a better understanding of what I’m trying to do

```html
<!DOCTYPE html>
<html lang="en">
<head>
<meta charset="UTF-8">
<title>Gilded Vantages – Business Card</title>
<link href="https://fonts.googleapis.com/css2?family=EB+Garamond:wght@400;500&family=Playball&family=Questrial&display=swap" rel="stylesheet">
<style>
  :root {
    --backdrop: #2b2b2b;
    --card-black: #050505;
    --card-white: #ffffff;
    --gold: #b89a3e;
    --gold-light: #d4bb62;
    --ink: #151515;
    --paper-text: #f4f4f4;
    --photo-sky: #8db4d6;
    --photo-wall: #3c4653;
    --photo-green: #5a6b3a;
  }
  * { margin: 0; padding: 0; box-sizing: border-box; }
  html, body {
    width: 1200px; height: 689px; overflow: hidden;
    background: var(--backdrop);
  }
  .canvas {
    position: relative; width: 1200px; height: 689px;
    display: flex; align-items: center; justify-content: center; gap: 40px;
  }
  .card {
    position: relative; width: 525px; height: 300px;
    border-radius: 22px; overflow: hidden;
    border: 2px solid var(--gold);
    box-shadow: 0 18px 40px rgba(0,0,0,0.45);
  }

  /* Front */
  .card-front {
    background: var(--card-black);
    display: flex; flex-direction: column; align-items: center; justify-content: center;
    gap: 22px;
  }
  .front-name {
    text-align: center;
    font-family: "EB Garamond", serif; font-weight: 400;
    font-size: 54px; line-height: 1; color: var(--gold-light);
  }
  .front-tagline {
    text-align: center;
    font-family: "EB Garamond", serif; font-size: 18px; line-height: 1.3;
    color: var(--paper-text);
  }

  /* Back */
  .card-back { background: var(--card-white); }
  .back-photo {
    position: absolute; right: 40px; top: 34px;
    width: 230px; height: 230px; border-radius: 50%;
    background:
      linear-gradient(180deg, var(--photo-sky) 0%, var(--photo-wall) 22%, var(--photo-wall) 62%, var(--photo-green) 100%);
  }
  .back-info {
    position: absolute; left: 34px; top: 56px; width: 250px;
  }
  .person-name {
    font-family: "Playball", cursive; font-weight: 400; font-size: 34px; line-height: 1.05;
    color: var(--gold);
  }
  .person-role {
    font-family: "Questrial", sans-serif; font-size: 17px;
    color: var(--ink); margin-top: 2px;
  }
  .contact-list { list-style: none; margin-top: 18px; }
  .contact-item {
    display: flex; align-items: center; gap: 8px;
    font-family: "Questrial", sans-serif; font-size: 16px;
    color: var(--ink); margin-bottom: 5px;
  }
  .contact-icon { width: 14px; height: 14px; flex: none; }
  .service-note {
    margin-top: 18px;
    font-family: "EB Garamond", serif; font-size: 17px; line-height: 1.25;
    color: var(--gold);
  }
</style>
</head>
<body>
  <main class="canvas">
    <section class="card card-front">
      <h1 class="front-name">Gilded<br>Vantages</h1>
      <p class="front-tagline">Gilded Vantages Custom<br>Plantation Shutters Motorized<br>Architectural Shading Systems</p>
    </section>

    <section class="card card-back">
      <div class="back-info">
        <h2 class="person-name">Daniel Forsythe</h2>
        <p class="person-role">Owner</p>
        <ul class="contact-list">
          <li class="contact-item">
            <svg class="contact-icon" viewBox="0 0 24 24"><path fill="#b89a3e" d="M6.6 10.8a15.1 15.1 0 0 0 6.6 6.6l2.2-2.2c.3-.3.7-.4 1-.2 1.1.4 2.3.6 3.6.6.6 0 1 .4 1 1V20c0 .6-.4 1-1 1A17 17 0 0 1 3 4c0-.6.4-1 1-1h3.5c.6 0 1 .4 1 1 0 1.3.2 2.5.6 3.6.1.3 0 .7-.2 1z"/></svg>
            919-482-7034
          </li>
          <li class="contact-item">
            <svg class="contact-icon" viewBox="0 0 24 24"><path fill="#b89a3e" d="M2 5h20v14H2z"/><path fill="none" stroke="#fff" stroke-width="1.6" d="M2 5l10 8 10-8"/></svg>
            GildedVantages.com
          </li>
        </ul>
        <p class="service-note">Custom Interior &amp; Exterior<br>Window Treatments<br>By Appointment</p>
      </div>
      <div class="back-photo" role="img" aria-label="Photo of a home's covered front porch with white columns, dark exterior shades and landscaped shrubs"></div>
    </section>
  </main>
</body>
</html>
```